Business Card Design Project

We are not a new company, but renamed to "Norvanta Kitchens" last year. We specialize in modern high-end cabinetry imports. We would like to communicate a sense of quality and cutting edge technology. Ideally the design would incorporate our logo colors, silver, red and preferably a black, matte background. Though we are open to suggestions.
Logo is attached.
Edit: I have attached rough drafts of the previous cards, this way you will have all necessary content that needs to go on the cards.
Reason: We have received a lot of great designs, but due to the sheer number we couldn't respond to all. We will extend the deadline for another 7 days to finalize and provide feedback to designers.
Thank you for your hard work!
Industry/Entity Type
Business
Look and feel
Each slider illustrates characteristics of the customer's brand and the style your logo design should communicate.

```html
<!DOCTYPE html>
<html lang="en">
<head>
<meta charset="utf-8">
<title>Norvanta Kitchens — Business Card</title>
<link rel="stylesheet" href="https://fonts.googleapis.com/css2?family=Cinzel:wght@400;700&display=swap">
<style>
  :root {
    --backdrop: #5a3722;
    --card-dark-core: #4b4b4d;
    --card-dark-edge: #121213;
    --panel-light: #ffffff;
    --panel-light-shade: #cfcfcf;
    --wordmark-silver: #d9d9d9;
    --accent-red: #c8141c;
    --ink: #1e1e1e;
    --ink-muted: #8a8a8a;
  }
  html, body {
    margin: 0;
    padding: 0;
    width: 1200px;
    height: 750px;
    overflow: hidden;
    background: var(--backdrop);
  }
  .canvas {
    position: relative;
    width: 1200px;
    height: 750px;
  }
  .card {
    position: absolute;
    left: 276px;
    width: 648px;
    height: 347px;
    display: block;
  }
  .card--front { top: 24px; }
  .card--back { top: 392px; }
  .wordmark {
    font-family: "Cinzel", serif;
    font-weight: 700;
    font-size: 31px;
    letter-spacing: 1px;
    fill: var(--wordmark-silver);
  }
  .holder-name {
    font-family: "Cinzel", serif;
    font-weight: 400;
    font-size: 20px;
    letter-spacing: 1px;
    fill: var(--ink);
  }
  .holder-role {
    font-family: "Cinzel", serif;
    font-weight: 400;
    font-size: 12px;
    fill: var(--ink-muted);
  }
  .contact-label {
    font-family: "Cinzel", serif;
    font-weight: 400;
    font-size: 12px;
    fill: var(--ink);
  }
</style>
</head>
<body>
<main class="canvas">

  <svg class="card card--front" viewBox="0 0 553 296" aria-label="Business card front">
    <defs>
      <clipPath id="front-shape"><rect width="553" height="296" rx="18"/></clipPath>
      <radialGradient id="front-core" cx="50%" cy="40%" r="60%">
        <stop offset="0" stop-color="var(--card-dark-core)"/>
        <stop offset="1" stop-color="var(--card-dark-edge)"/>
      </radialGradient>
      <linearGradient id="front-panel-left" x1="0" x2="1">
        <stop offset="0" stop-color="var(--panel-light-shade)"/>
        <stop offset="0.5" stop-color="var(--panel-light)"/>
        <stop offset="1" stop-color="var(--panel-light-shade)"/>
      </linearGradient>
    </defs>
    <g clip-path="url(#front-shape)">
      <rect class="front-field" width="553" height="296" fill="url(#front-core)"/>
      <path class="side-panel side-panel--left" d="M0,0 H24 C46,70 46,226 24,296 H0 Z" fill="url(#front-panel-left)"/>
      <path class="side-panel side-panel--right" d="M553,0 H529 C507,70 507,226 529,296 H553 Z" fill="url(#front-panel-left)"/>
    </g>
    <rect class="brand-square" x="269" y="112" width="14" height="14" fill="var(--accent-red)"/>
    <text class="wordmark" x="276.5" y="182" text-anchor="middle">Norvanta Kitchens</text>
  </svg>

  <svg class="card card--back" viewBox="0 0 553 296" aria-label="Business card back">
    <defs>
      <clipPath id="back-shape"><rect width="553" height="296" rx="18"/></clipPath>
      <linearGradient id="back-field" x1="0" y1="0" x2="0" y2="1">
        <stop offset="0" stop-color="#ffffff"/>
        <stop offset="1" stop-color="#e6e6e6"/>
      </linearGradient>
      <linearGradient id="back-panel" x1="0" x2="1">
        <stop offset="0" stop-color="var(--card-dark-edge)"/>
        <stop offset="0.5" stop-color="var(--card-dark-core)"/>
        <stop offset="1" stop-color="var(--card-dark-edge)"/>
      </linearGradient>
    </defs>
    <g clip-path="url(#back-shape)">
      <rect class="back-field" width="553" height="296" fill="url(#back-field)"/>
      <path class="side-panel side-panel--left" d="M0,0 H18 C44,80 44,216 18,296 H0 Z" fill="url(#back-panel)"/>
      <path class="side-panel side-panel--right" d="M553,0 H535 C509,80 509,216 535,296 H553 Z" fill="url(#back-panel)"/>
    </g>
    <text class="holder-name" x="78" y="130">Marcus Feld</text>
    <text class="holder-role" x="146" y="146">Director</text>
    <text class="contact-label" x="62" y="190">Address:</text>
    <text class="contact-label" x="62" y="205">Phone:</text>
    <text class="contact-label" x="62" y="220">Cell:</text>
    <text class="contact-label" x="62" y="235">Fax:</text>
    <text class="contact-label" x="62" y="250">Email:</text>
  </svg>

</main>
</body>
</html>
```